Flyer: Steady Steps, Bright Days

Please create a two (2) page flyer. We welcome minor updates/ changes to the Steady Steps Bright Days flyer that is attached as a word document. We are aiming for the same general look and feel as the original PDF attached (please note that we have updated the content and would like the designers to use what is listed in the word document).
We encourage you to provide multiple versions using pictures of different people we have on hand. Our team currently likes how the lady in the picture is looking in the direction of the text - we encourage designers to please flip the photo if needed to make this possible. We also give the permission to crop the photos as needed to fit the design better aesthetically. In addition, the team wondered about having a pdf file that allows the user to easily change out the graphic between different photos to reflect different communities best—not sure if that is as easy as it sounds. Please remember to include the funding statement - you can find it within both of the current documents. For more information about our project, please visit https://novelmarrow.org/wellness-path/

```html
<!DOCTYPE html>
<html lang="en">
<head>
<meta charset="utf-8">
<title>Steady Steps, Bright Days – Flyer</title>
<link href="https://fonts.googleapis.com/css2?family=Signika:wght@500;600;700&family=Roboto+Condensed:ital,wght@0,400;0,500;0,700;1,400&display=swap" rel="stylesheet">
<style>
:root{
  --stage:#6d6e71;
  --paper:#fcf5ef;
  --paper-tint:#f3e6dc;
  --maroon:#8e3b36;
  --brick:#a24b40;
  --rose:#c99a90;
  --teal:#3f9ea6;
  --ink:#2a2322;
  --ink-soft:#4a3f3d;
  --white:#ffffff;
}
*{box-sizing:border-box;margin:0;padding:0}
html,body{width:1200px;height:793px;overflow:hidden;background:var(--stage)}
body{position:relative;font-family:"Roboto Condensed",Arial,sans-serif;color:var(--ink)}
.page{position:absolute;top:84px;width:490px;height:635px;background:var(--paper);overflow:hidden;box-shadow:0 3px 10px rgba(0,0,0,.35)}
.page--front{left:75px}
.page--back{left:626px}
.abs{position:absolute}

/* shared */
.brand{display:flex;align-items:center;gap:6px;color:var(--teal);font-family:"Roboto Condensed",Arial,sans-serif;font-weight:700;text-transform:uppercase;line-height:1.05}
.brand__mark{width:22px;height:22px;border-radius:50%;background:var(--teal);flex:none}
.pulse-line{position:absolute}

/* front */
.front__pattern{left:210px;top:0;width:280px;height:635px;background:linear-gradient(180deg,var(--paper) 0%,var(--paper-tint) 45%,var(--paper) 100%)}
.front__photo{left:0;top:110px;width:250px;height:525px;
  background:radial-gradient(ellipse 70% 55% at 45% 45%,#b88c7b 0%,#d7b6a6 40%,#e9d3c6 65%,rgba(252,245,239,0) 92%),
             linear-gradient(180deg,rgba(252,245,239,0) 0%,#e6cfc2 50%,#d9b9ab 100%);}
.front__brand{left:24px;top:34px;font-size:12px}
.front__title{right:18px;top:22px;text-align:right;font-family:"Signika",sans-serif;font-weight:700;font-size:36px;line-height:35px;color:var(--maroon)}
.front__banner{left:222px;top:108px;width:268px;height:30px;background:var(--maroon);color:var(--white);font-weight:700;font-size:9px;display:flex;align-items:center;padding-left:14px}
.front__banner::before{content:"";position:absolute;left:-8px;top:0;border-top:15px solid transparent;border-bottom:15px solid transparent;border-right:8px solid var(--maroon)}
.front__intro{left:222px;top:145px;width:250px;font-size:9px;line-height:10.5px;text-align:right;color:var(--ink)}
.stat{position:absolute;top:198px;display:flex;align-items:flex-start;gap:6px}
.stat__icon{width:48px;height:34px;background:var(--maroon);border-radius:8px 14px 10px 6px;margin-top:6px}
.stat__icon--group{width:36px;height:42px;border-radius:4px}
.stat__num{font-family:"Signika",sans-serif;font-weight:600;font-size:25px;line-height:26px;color:var(--maroon);border-bottom:1px solid var(--maroon);text-align:center}
.stat__label{font-size:6.8px;line-height:7.6px;text-align:right;margin-top:2px}
.stat--one{left:220px}
.stat--two{left:352px}
.front__risk-heading{right:18px;top:263px;text-align:right;font-family:"Signika",sans-serif;font-weight:500;font-size:13.5px;line-height:15px;color:var(--brick);text-transform:uppercase}
.risk-list{right:16px;top:298px;list-style:none;text-align:right}
.risk-list li{font-size:11.5px;line-height:17px;color:var(--ink);display:flex;justify-content:flex-end;align-items:center;gap:6px}
.risk-list svg{width:10px;height:10px}
.front__pill{left:242px;top:353px;width:228px;height:22px;border-radius:11px;background:var(--maroon);color:var(--white);font-size:8.5px;font-weight:500;display:flex;align-items:center;justify-content:center;letter-spacing:.1px}
.steps{right:14px;top:381px;list-style:none;width:240px}
.steps li{display:flex;justify-content:flex-end;gap:6px;font-size:8px;line-height:9.2px;text-align:right;margin-bottom:3.6px}
.steps li::after{content:"";flex:none;width:6px;height:6px;border-radius:50%;border:1.4px solid var(--rose);background:var(--paper);margin-top:1.5px}
.front__note{right:22px;top:559px;text-align:right;font-style:italic;font-size:7.8px;line-height:9.4px;color:var(--brick)}
.front__pulse{left:120px;top:586px;width:370px;height:24px}
.front__more{right:22px;top:608px;text-align:right;font-size:8.8px;line-height:10.5px}
.front__more strong{font-weight:700}

/* back */
.back__photo{right:0;border-radius:4px;position:absolute}
.back__photo--top{top:0;width:230px;height:205px;background:radial-gradient(ellipse 65% 60% at 55% 50%,#b78a78 0%,#cfac9c 40%,#e8d6cb 70%,rgba(252,245,239,0) 95%)}
.back__photo--mid{top:175px;width:190px;height:180px;background:radial-gradient(ellipse 60% 60% at 60% 50%,#8f5e50 0%,#b58574 40%,#ddc3b6 70%,rgba(252,245,239,0) 95%)}
.back__photo--low{top:312px;width:215px;height:300px;background:radial-gradient(ellipse 60% 55% at 55% 45%,#7d6a66 0%,#a7918a 35%,#d58a70 55%,rgba(252,245,239,0) 92%)}
.back__title{left:17px;top:24px;font-family:"Signika",sans-serif;font-weight:600;font-size:13px;line-height:17px;color:var(--maroon)}
.back__rule{left:17px;top:61px;width:128px;height:5px;background:var(--maroon)}
.back__intro{left:17px;top:72px;width:262px;font-size:8.6px;line-height:10.4px;color:var(--ink)}
.back__intro p+p{margin-top:8px}
.back__banner{left:0;top:167px;width:205px;height:22px;background:var(--maroon);color:var(--white);font-size:10px;font-weight:500;display:flex;align-items:center;padding-left:15px;clip-path:polygon(0 0,100% 0,93% 100%,0 100%)}
.doctor-list{left:16px;top:193px;width:290px;list-style:none}
.doctor-list li{position:relative;padding-left:26px;margin-bottom:5px;font-size:7.2px;line-height:8.6px}
.doctor-list .ico{position:absolute;left:0;top:0;width:19px;height:19px}
.doctor-list b{color:var(--maroon);font-weight:700}
.doctor-list .lead{color:var(--maroon)}
.doctor-list ul{list-style:none;margin-top:1px}
.doctor-list ul li{padding-left:7px;margin:0;font-size:7.2px}
.doctor-list ul li::before{content:"•";position:absolute;left:0}
.back__pill{left:11px;top:448px;width:205px;height:22px;border-radius:11px;background:var(--maroon);color:var(--white);font-size:10px;font-weight:500;display:flex;align-items:center;padding-left:14px}
.other-list{left:28px;top:474px;width:370px;list-style:none}
.other-list li{position:relative;padding-left:11px;font-size:7.2px;line-height:8px;margin-bottom:2.6px}
.other-list li::before{content:"";position:absolute;left:0;top:1.5px;width:5px;height:5px;border-radius:50%;border:1.3px solid var(--rose)}
.back__brand{left:348px;top:544px;font-size:9.5px}
.back__brand .brand__mark{width:18px;height:18px}
.back__pulse{left:300px;top:582px;width:190px;height:22px}
.back__funding{left:16px;top:602px;width:460px;font-size:5.9px;line-height:7.2px;color:var(--ink)}
</style>
</head>
<body>

<!-- Page one -->
<section class="page page--front" aria-label="Flyer page one">
  <div class="abs front__pattern" role="img" aria-label="Soft woven geometric background pattern in cream and blush tones"></div>
  <div class="abs front__photo" role="img" aria-label="Portrait of an elder woman in a floral blouse and shell necklace, facing the text"></div>

  <div class="abs brand front__brand"><span class="brand__mark"></span><span>Novel Marrow<br>Elder Network</span></div>

  <h1 class="abs front__title">Steady Steps,<br>Bright Days…</h1>

  <div class="abs front__banner">Keep Your Heart and Body Healthy to Protect Your Brain</div>

  <p class="abs front__intro">Everyone slows down as they get older, both in body and mind. Big changes in memory or thinking that make it hard to get through the day are not a normal part of aging. These changes could be signs of early dementia or Alzheimer’s disease.</p>

  <div class="stat stat--one">
    <div class="stat__icon" role="img" aria-label="Map of the United States"></div>
    <div>
      <div class="stat__num">1 in 9</div>
      <div class="stat__label">People in the U.S.<br>ages 65+ has<br>Alzheimer’s dementia</div>
    </div>
  </div>
  <div class="stat stat--two">
    <div class="stat__icon stat__icon--group" role="img" aria-label="Group of people figures"></div>
    <div>
      <div class="stat__num">1 in 3</div>
      <div class="stat__label">American Indian<br>people ages 65+<br>develops dementia</div>
    </div>
  </div>

  <h2 class="abs front__risk-heading">You are more at risk of developing<br>dementia if you have:</h2>
  <ul class="abs risk-list">
    <li>High Blood Pressure <svg viewBox="0 0 10 10"><circle cx="5" cy="5" r="4.2" fill="none" stroke="#a24b40" stroke-width="1"/><path d="M3 5.2l1.5 1.5L7.2 3.8" fill="none" stroke="#a24b40" stroke-width="1"/></svg></li>
    <li>Diabetes or <svg viewBox="0 0 10 10"><circle cx="5" cy="5" r="4.2" fill="none" stroke="#a24b40" stroke-width="1"/><path d="M3 5.2l1.5 1.5L7.2 3.8" fill="none" stroke="#a24b40" stroke-width="1"/></svg></li>
    <li>You Smoke Cigarettes <svg viewBox="0 0 10 10"><circle cx="5" cy="5" r="4.2" fill="none" stroke="#a24b40" stroke-width="1"/><path d="M3 5.2l1.5 1.5L7.2 3.8" fill="none" stroke="#a24b40" stroke-width="1"/></svg></li>
  </ul>

  <div class="abs front__pill">YOU CAN PROTECT YOUR BODY, HEART, AND MIND</div>
  <ul class="abs steps">
    <li><span>Schedule a “wellness” visit and health screenings<br>every year with your doctor, even if you feel ok</span></li>
    <li><span>Keep a healthy blood pressure</span></li>
    <li><span>Be active or walk every day</span></li>
    <li><span>Maintain a healthy weight for your body size</span></li>
    <li><span>Eat a healthier diet with more fresh vegetables,<br>fruits, whole grains, and fish</span></li>
    <li><span>Stop smoking cigarettes or chewing tobacco</span></li>
    <li><span>Get help managing your high blood pressure,<br>diabetes, or to lose extra weight</span></li>
    <li><span>Talk to your doctor about how you feel because your<br>mental health can affect your brain and physical health</span></li>
    <li><span>If it is hard for you to get through the day because<br>of forgetfulness or memory problems, see your<br>doctor right away</span></li>
  </ul>
  <p class="abs front__note">You can do these things today to protect your mind and reduce<br>the risk of or slow down dementia.</p>

  <svg class="pulse-line front__pulse" viewBox="0 0 370 24" preserveAspectRatio="none">
    <polyline points="0,14 260,14 266,14 270,4 275,22 280,8 284,14 370,14" fill="none" stroke="#8e3b36" stroke-width="1"/>
  </svg>
  <p class="abs front__more">For more information about our project, please visit<br><strong>https://novelmarrow.org/wellness-path/</strong></p>
</section>

<!-- Page two -->
<section class="page page--back" aria-label="Flyer page two">
  <div class="back__photo back__photo--top" role="img" aria-label="Portrait of a smiling elder woman with glasses and earrings"></div>
  <div class="back__photo back__photo--mid" role="img" aria-label="Portrait of a smiling middle-aged woman"></div>
  <div class="back__photo back__photo--low" role="img" aria-label="Portrait of an elder man with glasses over a warm watercolor wash"></div>

  <h1 class="abs back__title">The River of Life Flows Through Your Heart<br>to Protect Your Mind and Body</h1>
  <div class="abs back__rule"></div>
  <div class="abs back__intro">
    <p>Your heart health plays a big part in the health of your brain. Your heart is like the start of a flowing river. Blood vessels that take blood to and from your heart are like connected streams that flow through your body. They feed your brain with oxygen and energy.</p>
    <p>You can do things to keep the streams freely flowing through your body, so your heart and brain stay strong and healthy.</p>
  </div>

  <div class="abs back__banner">WORKING WITH YOUR DOCTOR</div>
  <ul class="abs doctor-list">
    <li><svg class="ico" viewBox="0 0 20 20"><circle cx="10" cy="10" r="9.5" fill="#c99a90"/><circle cx="10" cy="10" r="7.5" fill="#8e3b36"/><path d="M7 6v4a3 3 0 006 0V6M10 13v2" fill="none" stroke="#fff" stroke-width="1.2"/></svg>
      <span class="lead"><b>Make an appointment</b> for a “wellness” checkup with your<br>doctor every year</span>
      <ul>
        <li>You will get tests and screenings to make sure you are healthy</li>
        <li>They are usually free with Senior Care Plan or the Tribal Health Clinic</li>
        <li>If you have concerns about your memory, talk to your doctor</li>
      </ul>
    </li>
    <li><svg class="ico" viewBox="0 0 20 20"><circle cx="10" cy="10" r="9.5" fill="#c99a90"/><circle cx="10" cy="10" r="7.5" fill="#8e3b36"/><path d="M10 5c2 3 3 4.5 3 6a3 3 0 01-6 0c0-1.5 1-3 3-6z" fill="#fff"/></svg>
      <span class="lead"><b>Have your blood pressure checked</b> and know your<br>numbers</span>
      <ul>
        <li>Your blood pressure should be less than 120/80 mmHg (120 over 80)</li>
        <li>If you do not know how to take your blood pressure, ask your<br>doctor to show you</li>
      </ul>
    </li>
    <li><svg class="ico" viewBox="0 0 20 20"><circle cx="10" cy="10" r="9.5" fill="#c99a90"/><circle cx="10" cy="10" r="7.5" fill="#8e3b36"/><circle cx="10" cy="7" r="1.8" fill="#fff"/><path d="M7 14l1.5-4h3l1.5 4z" fill="#fff"/></svg>
      <span class="lead"><b>Have your weight checked</b> regularly and know your number.<br>If you need to lose extra weight, ask your doctor about:</span>
      <ul>
        <li>The right number of calories for your body</li>
        <li>Ideas for healthier food choices</li>
        <li>Support for losing weight</li>
      </ul>
    </li>
    <li><svg class="ico" viewBox="0 0 20 20"><circle cx="10" cy="10" r="9.5" fill="#c99a90"/><circle cx="10" cy="10" r="7.5" fill="#8e3b36"/><rect x="5" y="10" width="10" height="2.2" fill="#fff"/><path d="M13 6c1 1 1 2.5 0 3.5" fill="none" stroke="#fff" stroke-width="1"/></svg>
      <span class="lead"><b>If you smoke cigarettes or chew tobacco,</b> ask about medicine,<br>counseling, or help to stop</span>
    </li>
    <li><svg class="ico" viewBox="0 0 20 20"><circle cx="10" cy="10" r="9.5" fill="#c99a90"/><circle cx="10" cy="10" r="7.5" fill="#8e3b36"/><path d="M10 14.5l-4-4a2.3 2.3 0 014-2.5 2.3 2.3 0 014 2.5z" fill="#fff"/></svg>
      <span><b>If you do not have diabetes,</b> <span class="lead">have your blood sugar level checked<br>during your visit.</span> Your blood sugar should be less than 100 mg/dL<br>when you have not eaten.</span>
    </li>
    <li><svg class="ico" viewBox="0 0 20 20"><circle cx="10" cy="10" r="9.5" fill="#c99a90"/><circle cx="10" cy="10" r="7.5" fill="#8e3b36"/><path d="M5.5 6.5h9v6h-5l-2.5 2v-2h-1.5z" fill="#fff"/></svg>
      <span><b>Talk with your doctor</b> <span class="lead">about all the medicines and vitamins you take.</span><br>Your doctor can make sure they do not cause any problems with your<br>memory, sleep, or brain function.</span>
    </li>
  </ul>

  <div class="abs back__pill">OTHER STEPS YOU CAN TAKE</div>
  <ul class="abs other-list">
    <li>Aim for 20 minutes of physical activity a day or 2 1/2 hours a week</li>
    <li>Eat less salt, sugar, red meat, and highly processed or packaged foods</li>
    <li>Read food labels to see how much salt (sodium) or fat is in your food</li>
    <li>Manage extra weight by making small changes. Losing a few pounds<br>makes a difference</li>
    <li>Limit alcohol. No more than 1 drink per day for women and 2 for men</li>
    <li>Take your medicine for blood pressure, diabetes, and other problems<br>even if you feel good</li>
    <li>Get at least seven hours of sleep each night. Talk to your doctor if you<br>have trouble sleeping</li>
    <li>Keep your mind active. Visit with people in your community, help plan tribal events,<br>go to your senior center, teach your language, play cards, or start a new hobby.</li>
  </ul>

  <div class="abs brand back__brand"><span class="brand__mark"></span><span>Novel Marrow<br>Elder Network</span></div>
  <svg class="pulse-line back__pulse" viewBox="0 0 190 22" preserveAspectRatio="none">
    <polyline points="0,14 40,14 44,14 48,3 53,21 58,7 62,14 190,14" fill="none" stroke="#8e3b36" stroke-width="1"/>
  </svg>
  <p class="abs back__funding">This product is supported by the Federal Office of Community Health (FOCH) of the National Health Department (NHD) as part of a financial assistance award totaling $348,711 with 100 percent funded by FOCH/NHD. The contents are those of the author(s) and do not necessarily represent the official views of, nor an endorsement, by FOCH/NHD, or the U.S. Government.</p>
</section>

</body>
</html>
```